Pamphlet for introducing people to our church

I would like a church pamphlet designed, that includes the content in file "tovik-pamphlet.txt".

I am looking for a design that will incorporate the content in a professional and creative manner.

You do not have to use the content in any specific order, but I am relying on your skill and design knowledge to organize everything in an artistic and effective way.

Target Market(s)

Everyone

Industry/Entity Type

Religious

Requirements
Must have
• logo, use of content provided, use of branding (logo colors)
Nice to have
• More images where necessary
Should not have
• cross

```html
<!DOCTYPE html>
<html lang="en">
<head>
<meta charset="utf-8">
<title>TOVIK – A Voice to the Nations</title>
<link rel="stylesheet" href="https://fonts.googleapis.com/css2?family=Cinzel:wght@700&family=Kaushan+Script&family=Lato:wght@400;700;900&display=swap">
<style>
  :root {
    --navy-deep: #0c2c55;
    --navy: #0f416e;
    --orange: #f39019;
    --white: #ffffff;
    --mist: #e3e5e8;
    --backdrop: #ececec;
  }
  * { margin: 0; padding: 0; box-sizing: border-box; }
  html, body { width: 1062px; height: 1200px; overflow: hidden; background: var(--backdrop); }
  body { font-family: "Lato", sans-serif; }

  .pamphlet {
    position: absolute; left: 126px; top: 28px;
    width: 809px; height: 1143px;
    background: var(--navy-deep);
    overflow: hidden;
    box-shadow: 0 6px 18px rgba(0,0,0,.18);
  }
  .hero-photo {
    position: absolute; left: 0; top: 0; width: 809px; height: 610px;
    background:
      radial-gradient(ellipse at 30% 25%, rgba(255,255,255,.85), rgba(255,255,255,0) 55%),
      linear-gradient(180deg, #e9d9e2 0%, #c9a9a9 35%, #6d4a45 62%, #2c1f22 100%);
  }
  .panels { position: absolute; left: 0; top: 0; width: 809px; height: 1143px; }

  .headline { position: absolute; left: 45px; top: 52px; color: var(--navy-deep); }
  .headline-main { font-family: "Cinzel", serif; font-weight: 700; font-size: 70px; line-height: 1; letter-spacing: 1px; }
  .headline-small { font-family: "Kaushan Script", cursive; font-size: 34px; position: absolute; left: 0; top: 80px; }
  .headline-script { font-family: "Kaushan Script", cursive; color: var(--orange); font-size: 100px; position: absolute; left: 110px; top: 62px; white-space: nowrap; }

  .brand-tab {
    position: absolute; left: 550px; top: 0; width: 242px; height: 208px;
    background: var(--navy-deep); border-radius: 0 0 16px 16px;
    display: flex; align-items: center; justify-content: center; gap: 12px;
  }
  .brand-dot { width: 18px; height: 18px; border-radius: 50%; background: var(--orange); }
  .brand-name { font-family: "Lato", sans-serif; font-weight: 700; font-size: 52px; color: var(--white); letter-spacing: 2px; }

  .about {
    position: absolute; left: 43px; top: 647px; width: 317px;
    color: var(--white); font-size: 15.2px; line-height: 19.6px; text-align: justify;
  }
  .about p + p { margin-top: 19.6px; }
  .about .name { color: var(--orange); font-weight: 700; }

  .ministries { position: absolute; left: 451px; top: 650px; width: 320px; color: var(--white); }
  .ministries h2 { color: var(--orange); font-weight: 900; font-size: 26px; letter-spacing: .5px; margin-bottom: 12px; }
  .ministry { position: relative; padding-left: 19px; margin-bottom: 12px; font-size: 15.2px; line-height: 19.5px; }
  .ministry::before {
    content: ""; position: absolute; left: 0; top: 4px;
    border-left: 12px solid var(--orange); border-top: 6.5px solid transparent; border-bottom: 6.5px solid transparent;
  }
  .ministry h3 { color: var(--orange); font-weight: 700; font-size: 15.8px; }

  .service-box {
    position: absolute; left: 446px; top: 892px; width: 327px; height: 113px;
    background: var(--orange); border-radius: 14px;
    padding: 7px 0 0 21px; color: var(--navy-deep); font-size: 15.6px; line-height: 19.6px;
  }
  .service-box strong { font-weight: 700; }

  .help-band {
    position: absolute; left: 0; top: 1058px; width: 809px; height: 85px;
    background: var(--mist); text-align: center; padding-top: 14px;
    font-size: 20px; line-height: 26px; font-weight: 700;
  }
  .help-band .invite { color: var(--orange); }
  .help-band .contact { color: var(--navy-deep); font-weight: 900; }
</style>
</head>
<body>
<main class="pamphlet">
  <div class="hero-photo" role="img" aria-label="Congregation in worship with raised hands facing a brightly lit stage"></div>

  <svg class="panels" width="809" height="1143" viewBox="0 0 809 1143" aria-hidden="true">
    <polygon points="0,576 404,607 404,1143 0,1143" fill="var(--navy-deep)"/>
    <polygon points="404,607 809,576 809,1143 404,1143" fill="var(--navy)"/>
    <polyline points="0,571 404,603 809,571" fill="none" stroke="var(--orange)" stroke-width="7"/>
  </svg>

  <header class="headline">
    <div class="headline-main">A VOICE</div>
    <div class="headline-small">to the</div>
    <div class="headline-script">Nations</div>
  </header>

  <div class="brand-tab">
    <span class="brand-dot"></span>
    <span class="brand-name">TOVIK</span>
  </div>

  <section class="about">
    <p><span class="name">TOVIK</span> is a gathering of believers whose purpose is to seek the face of God for an authentic restoration of the church as a body of born again believers around the world. As a gathering of believers, TOVIK seeks an awakening of the mind founded on the precepts and teachings of Jesus Christ.</p>
    <p>The modern church has replaced the simple and Kingdom centered principles of Jesus's disciples with complacent and compromised teachings on earthly prosperity. We believe in humbly seeking God without motive to use God or His Word for our own gain. The end times church will experience a glorious revival, renewed love and zeal for true discipleship, faith, and godliness as Jesus intended for us.</p>
  </section>

  <section class="ministries">
    <h2>MINISTRIES:</h2>
    <div class="ministry">
      <h3>Kingdom seeds (Children's ministry)</h3>
      <p>Children learn to be seeds of godliness in the world.</p>
    </div>
    <div class="ministry">
      <h3>School of pilgrims</h3>
      <p>Learn the basics of Christian faith and about God's purpose for your life.</p>
    </div>
    <div class="ministry">
      <h3>School of disciples</h3>
      <p>Deepen your knowledge of God's word and learn how to server him.</p>
    </div>
  </section>

  <aside class="service-box">
    <strong>Sunday Service:</strong><br>
    10:00am-12:30pm<br>
    Harbor Community Hall<br>
    58 Linden Street, Portland, ME 04101<br>
    <strong>Visit us at www.tovik.org</strong>
  </aside>

  <footer class="help-band">
    <div class="invite">If you need prayer or counseling give us a call at</div>
    <div class="contact">+1 207-555-0148 or email us at contact@cedargrove.org</div>
  </footer>
</main>
</body>
</html>
```